Creative & Professional Business Card for hair salon

We are looking to update our business cards. Our salon is creative, modern, progressive and professional and looking for a design that will reflect this.

```html
<!DOCTYPE html>
<html lang="en">
<head>
<meta charset="utf-8">
<title>Silver Lining – Business Cards</title>
<link rel="stylesheet" href="https://fonts.googleapis.com/css2?family=Quicksand:wght@400;500&family=Montserrat:ital,wght@0,500;0,600;1,500&display=swap">
<style>
  :root {
    --page: #eceae6;
    --card-white: #ffffff;
    --sky-light: #dceefa;
    --sky-mid: #b9dcf3;
    --blue-top: #92d2f0;
    --blue-bottom: #74c4ea;
    --ink: #5a8796;
    --ink-dark: #4a7584;
    --band-pale: #d6ecf8;
    --band-mid: #a9d9f2;
    --band-deep: #3db6e8;
    --rule: #7fa8b6;
    --dash: #8aa6b1;
  }
  * { box-sizing: border-box; margin: 0; padding: 0; }
  html, body { width: 1200px; height: 960px; overflow: hidden; }
  body {
    background: var(--page);
    font-family: "Montserrat", sans-serif;
    position: relative;
  }
  .card {
    position: absolute;
    top: 320px;
    width: 560px;
    height: 320px;
    border-radius: 4px;
    overflow: hidden;
    box-shadow: 0 6px 18px rgba(0,0,0,0.15);
  }

  /* Front: brand card */
  .brand-card { left: 20px; background: var(--card-white); }
  .brand-card .sky {
    position: absolute; inset: 0;
    background: radial-gradient(ellipse 260px 200px at 0% 100%, var(--sky-mid) 0%, var(--sky-light) 45%, rgba(255,255,255,0) 100%);
  }
  .brand-name {
    position: absolute; left: 110px; top: 118px;
    font-family: "Quicksand", sans-serif; font-weight: 400;
    color: var(--ink);
  }
  .brand-name .title-row { display: flex; align-items: center; gap: 14px; }
  .brand-dot { width: 18px; height: 18px; border-radius: 50%; background: var(--ink); flex: none; }
  .brand-name .title { font-size: 48px; line-height: 1.1; }
  .brand-name .sub { display: block; font-size: 22px; margin-top: 6px; text-align: right; }

  /* Back: appointment card */
  .appointment-card {
    left: 620px;
    background: linear-gradient(180deg, var(--blue-top), var(--blue-bottom));
  }
  .salon-name {
    position: absolute; left: 28px; top: 48px;
    display: flex; align-items: center; gap: 10px;
    font-family: "Quicksand", sans-serif; font-weight: 400;
    font-size: 30px; color: var(--ink);
  }
  .salon-name .dot { width: 12px; height: 12px; border-radius: 50%; background: var(--ink); flex: none; }
  .divider {
    position: absolute; left: 262px; top: 26px;
    width: 1px; height: 82px; background: var(--rule);
  }
  .contact {
    position: absolute; left: 278px; top: 26px;
    list-style: none; font-size: 11.5px; font-weight: 600; color: var(--ink-dark);
  }
  .contact li { display: flex; align-items: center; gap: 8px; height: 20px; white-space: nowrap; }
  .contact svg { width: 12px; height: 12px; flex: none; fill: var(--ink-dark); }
  .booking {
    position: absolute; left: 36px; right: 36px; top: 118px; height: 138px;
    background: var(--card-white);
    border: 1px dashed #9fb7c1;
  }
  .booking h2 {
    position: absolute; top: 10px; left: 0; right: 0; text-align: center;
    font-size: 12px; font-style: italic; font-weight: 500; color: var(--ink-dark);
  }
  .field {
    position: absolute; display: flex; align-items: flex-end; gap: 8px;
    font-size: 13px; font-style: italic; font-weight: 500; color: var(--ink-dark);
  }
  .field .line { flex: 1; border-bottom: 1px dashed var(--dash); height: 14px; }
  .field-for { left: 14px; right: 14px; top: 36px; }
  .field-date { left: 14px; width: 220px; top: 72px; }
  .field-time { left: 250px; right: 14px; top: 88px; }
  .footer-band {
    position: absolute; left: 0; right: 0; bottom: 0; height: 56px;
    background: linear-gradient(90deg, var(--band-pale) 0%, var(--band-pale) 45%, var(--band-mid) 75%, var(--band-deep) 100%);
  }
  .social {
    position: absolute; left: 14px; bottom: 20px;
    display: flex; align-items: center; gap: 7px;
    font-size: 12px; font-weight: 600; color: var(--ink-dark);
  }
  .social .box { width: 12px; height: 12px; background: var(--ink-dark); flex: none; }
</style>
</head>
<body>

<section class="card brand-card">
  <div class="sky" role="img" aria-label="Soft sky with light clouds fading in from the lower left corner"></div>
  <div class="brand-name">
    <div class="title-row">
      <span class="brand-dot"></span>
      <span class="title">Silver Lining</span>
    </div>
    <span class="sub">by Jo Marlowe</span>
  </div>
</section>

<section class="card appointment-card">
  <div class="salon-name"><span class="dot"></span>Silver Lining</div>
  <div class="divider"></div>
  <ul class="contact">
    <li><svg viewBox="0 0 12 12"><path d="M6 0a4 4 0 0 0-4 4c0 3 4 8 4 8s4-5 4-8a4 4 0 0 0-4-4zm0 5.5A1.5 1.5 0 1 1 6 2.5a1.5 1.5 0 0 1 0 3z"/></svg>12/40 Harbour Road, Maleny</li>
    <li><svg viewBox="0 0 12 12"><path d="M2.5 0.5l2 2-1.2 1.6c.8 1.7 2 2.9 3.6 3.6L8.5 6.5l2 2-1.5 2.5C4.5 10.5 1.5 7.5 0.5 2.5z"/></svg>07 5000 1234</li>
    <li><svg viewBox="0 0 12 12"><path d="M0 2.5h12v7H0zM1 3.2l5 3.4 5-3.4v-.2H1z"/></svg>hello@silverliningsalon.com.au</li>
    <li><svg viewBox="0 0 12 12"><circle cx="6" cy="6" r="5" fill="none" stroke="var(--ink-dark)" stroke-width="1.2"/><path d="M1 6h10M6 1v10" stroke="var(--ink-dark)" stroke-width="1"/></svg>www.silverliningsalon.com.au</li>
  </ul>

  <div class="booking">
    <h2>Your Next Appointment is</h2>
    <div class="field field-for">For <span class="line"></span></div>
    <div class="field field-date">Date <span class="line"></span></div>
    <div class="field field-time">Time <span class="line"></span></div>
  </div>

  <div class="footer-band" role="img" aria-label="Decorative flowing blue wave band along the bottom edge"></div>
  <div class="social"><span class="box"></span>SilverLiningbyJoMarlowe</div>
</section>

</body>
</html>
```